Electrical Services Flyer

We need to create a flyer which will be posted out across Melbourne to businesses to promote our new Electrical Services Division. Services we deliver include but are not limited to - Office Shop fit outs- Lighting and Lighting Automation - Exit and Emergency lighting - Body Corporate works- Thermal Imaging- Test and Tagging- Fault Diagnosis- Switchboard Maintenance/UpgradesFor more on our company please visit corvelmapower.com.au

Target Market(s)

Businesses

Colors

Designer to choose colors to be used in the design.

Requirements
Must have
• A modern look, simple clean eye catching.
• A clear way to contact the business
• 148 272
• Quote@corvelma.com.au
Nice to have
• A simple eye catching design that attracts the eye with a simple catchy line like "need an electrician?"

```html
<!DOCTYPE html>
<html lang="en">
<head>
<meta charset="utf-8">
<title>Corvelma Electrical Services Flyer</title>
<link href="https://fonts.googleapis.com/css2?family=Montserrat:wght@600;700;800&family=Lato:wght@400;700&display=swap" rel="stylesheet">
<style>
  :root {
    --orange: #f47f20;
    --blue: #2e3f97;
    --ink: #1d1d1d;
    --text: #2a2a2a;
    --white: #ffffff;
    --stage: #cfcfcf;
    --photo-a: #8d8f93;
    --photo-b: #c9ccd1;
  }
  * { margin: 0; padding: 0; box-sizing: border-box; }
  html, body { width: 1200px; height: 1200px; overflow: hidden; background: var(--stage); }
  .flyer {
    position: absolute; left: 182px; top: 13px;
    width: 929px; height: 1303px; background: var(--white);
    transform: scale(0.9); transform-origin: top left; overflow: hidden;
    font-family: 'Lato', sans-serif; color: var(--text);
  }
  .hero { position: absolute; left: 0; top: 0; width: 929px; height: 460px; }
  .brand { position: absolute; left: 542px; top: 429px; display: flex; align-items: center; gap: 14px; }
  .brand-dot { width: 100px; height: 100px; border-radius: 50%; background: var(--orange); }
  .brand-name { font-family: 'Montserrat', sans-serif; font-weight: 800; font-size: 38px; line-height: 1.05; color: var(--blue); }
  .headline { position: absolute; left: 46px; top: 468px; font-family: 'Montserrat', sans-serif; font-weight: 800; font-size: 66px; line-height: 62px; letter-spacing: 0.5px; }
  .headline .line-orange { color: var(--orange); display: block; }
  .headline .line-blue { color: var(--blue); display: block; }
  .feature { position: absolute; left: 45px; width: 495px; }
  .feature-icon { position: absolute; left: 0; width: 94px; height: 94px; border-radius: 50%; background: var(--orange); display: flex; align-items: center; justify-content: center; }
  .feature-title { position: absolute; left: 114px; top: 0; font-family: 'Montserrat', sans-serif; font-weight: 800; font-size: 18px; color: var(--orange); }
  .feature-body { position: absolute; left: 114px; top: 27px; width: 380px; font-size: 16px; line-height: 20px; text-align: justify; color: var(--text); }
  .divider { position: absolute; left: 159px; width: 376px; border-top: 2px dashed var(--blue); opacity: 0.8; }
  .services { position: absolute; left: 571px; top: 604px; width: 358px; height: 538px; background: linear-gradient(135deg, #f7892c, var(--orange) 55%, #ec7417); color: var(--white); }
  .services-bar { position: absolute; left: 0; top: 24px; width: 39px; height: 96px; background: var(--blue); }
  .services-title { position: absolute; left: 53px; top: 26px; font-family: 'Montserrat', sans-serif; line-height: 1; }
  .services-title .strong { display: block; font-weight: 800; font-size: 44px; color: var(--blue); }
  .services-title .light { display: block; font-weight: 600; font-size: 36px; color: var(--white); margin-top: 8px; letter-spacing: 1px; }
  .service-list { position: absolute; left: 32px; top: 152px; list-style: none; }
  .service-list li { display: flex; align-items: center; gap: 7px; font-size: 16.5px; height: 36.4px; }
  .contact { position: absolute; left: 0; top: 1161px; width: 929px; height: 142px; background: var(--blue); }
  .contact-tab { position: absolute; left: 0; top: 0; width: 182px; height: 142px; }
  .contact-dot { position: absolute; left: 46px; top: 24px; width: 92px; height: 92px; border-radius: 50%; background: var(--white); }
  .contact-title { position: absolute; left: 218px; top: 13px; font-family: 'Montserrat', sans-serif; font-weight: 600; font-size: 28px; letter-spacing: 1px; color: var(--white); }
  .contact-title span { color: var(--orange); }
  .contact-item { position: absolute; display: flex; align-items: flex-start; gap: 10px; color: var(--white); font-size: 16.5px; line-height: 21px; }
  .contact-item p { margin-bottom: 6px; }
</style>
</head>
<body>
<div class="flyer">
  <svg class="hero" viewBox="0 0 929 460" xmlns="http://www.w3.org/2000/svg">
    <defs>
      <linearGradient id="photoTone" x1="0" y1="0" x2="1" y2="1">
        <stop offset="0" stop-color="var(--photo-a)"/>
        <stop offset="1" stop-color="var(--photo-b)"/>
      </linearGradient>
    </defs>
    <polygon points="0,0 929,0 929,385 664,313 292,440 0,351" fill="url(#photoTone)" role="img" aria-label="Photo of two electricians in hard hats and hi-vis vests inspecting cabling at a job site"/>
    <polygon points="0,351 292,440 664,313 929,385 929,411 664,343 292,456 0,378" fill="var(--blue)"/>
  </svg>

  <div class="brand">
    <div class="brand-dot"></div>
    <div class="brand-name">Corvelma<br>Electrical</div>
  </div>

  <h1 class="headline"><span class="line-orange">NEED AN</span><span class="line-blue">ELECTRICIAN?</span></h1>

  <section class="feature" style="top:627px">
    <div class="feature-icon" style="top:29px">
      <svg width="52" height="52" viewBox="0 0 52 52" fill="none" stroke="#fff" stroke-width="4" stroke-linecap="round"><circle cx="22" cy="22" r="14"/><line x1="32" y1="32" x2="45" y2="45"/><circle cx="22" cy="18" r="4" fill="#fff" stroke="none"/><path d="M14 29c2-5 14-5 16 0" stroke-width="3"/></svg>
    </div>
    <h2 class="feature-title">CUSTOMER FOCUSED</h2>
    <p class="feature-body">We have built a reputation for over 55 years, with customer satisfaction as our number one priority. It comes to no surprise why thousands of Australians trust Corvelma Electrical for their electrical needs every year.</p>
  </section>
  <div class="divider" style="top:791px"></div>

  <section class="feature" style="top:825px">
    <div class="feature-icon" style="top:28px">
      <svg width="60" height="44" viewBox="0 0 60 44" fill="#fff"><circle cx="30" cy="9" r="7"/><circle cx="12" cy="13" r="6"/><circle cx="48" cy="13" r="6"/><path d="M20 44V26c0-6 4-9 10-9s10 3 10 9v18z"/><path d="M3 44V29c0-5 3-8 9-8 3 0 5 1 6 2v21z"/><path d="M57 44V29c0-5-3-8-9-8-3 0-5 1-6 2v21z"/></svg>
    </div>
    <h2 class="feature-title">QUALIFIED TEAM</h2>
    <p class="feature-body" style="top:35px">We have a fully qualified team of electricians and estimators who are motivated and ready to work. With our track record ranging across a wide variety of electrical work, it means we can handle just about any job.</p>
  </section>
  <div class="divider" style="top:987px"></div>

  <section class="feature" style="top:1024px">
    <div class="feature-icon" style="top:8px">
      <svg width="56" height="56" viewBox="0 0 56 56" fill="none" stroke="#fff" stroke-width="3.5"><circle cx="28" cy="28" r="24"/><path d="M28 14c-7 0-11 5-11 10 0 8 11 19 11 19s11-11 11-19c0-5-4-10-11-10z" fill="#fff" stroke="none"/><circle cx="28" cy="24" r="4" fill="var(--orange)" stroke="none"/></svg>
    </div>
    <h2 class="feature-title">LOCALLY OWNED</h2>
    <p class="feature-body" style="top:31px">We are locally owned and operated, working in all residential and commercial sectors around Victoria. With head office based in Oakleigh, we are mobile and able to reach all ends of our wonderful state.</p>
  </section>

  <aside class="services">
    <div class="services-bar"></div>
    <h2 class="services-title"><span class="strong">SERVICES</span><span class="light">WE DELIVER</span></h2>
    <ul class="service-list">
      <li><svg width="18" height="18" viewBox="0 0 18 18" fill="none" stroke="var(--blue)" stroke-width="2.4" stroke-linecap="round"><circle cx="8" cy="10" r="6.5"/><path d="M5 9.5l3 3 8-10"/></svg>Office Shop fit outs</li>
      <li><svg width="18" height="18" viewBox="0 0 18 18" fill="none" stroke="var(--blue)" stroke-width="2.4" stroke-linecap="round"><circle cx="8" cy="10" r="6.5"/><path d="M5 9.5l3 3 8-10"/></svg>Lighting and Lighting Automation</li>
      <li><svg width="18" height="18" viewBox="0 0 18 18" fill="none" stroke="var(--blue)" stroke-width="2.4" stroke-linecap="round"><circle cx="8" cy="10" r="6.5"/><path d="M5 9.5l3 3 8-10"/></svg>Exit and Emergency lighting</li>
      <li><svg width="18" height="18" viewBox="0 0 18 18" fill="none" stroke="var(--blue)" stroke-width="2.4" stroke-linecap="round"><circle cx="8" cy="10" r="6.5"/><path d="M5 9.5l3 3 8-10"/></svg>Body Corporate works</li>
      <li><svg width="18" height="18" viewBox="0 0 18 18" fill="none" stroke="var(--blue)" stroke-width="2.4" stroke-linecap="round"><circle cx="8" cy="10" r="6.5"/><path d="M5 9.5l3 3 8-10"/></svg>Thermal Imaging</li>
      <li><svg width="18" height="18" viewBox="0 0 18 18" fill="none" stroke="var(--blue)" stroke-width="2.4" stroke-linecap="round"><circle cx="8" cy="10" r="6.5"/><path d="M5 9.5l3 3 8-10"/></svg>Test and Tagging</li>
      <li><svg width="18" height="18" viewBox="0 0 18 18" fill="none" stroke="var(--blue)" stroke-width="2.4" stroke-linecap="round"><circle cx="8" cy="10" r="6.5"/><path d="M5 9.5l3 3 8-10"/></svg>Fault Diagnosis</li>
      <li><svg width="18" height="18" viewBox="0 0 18 18" fill="none" stroke="var(--blue)" stroke-width="2.4" stroke-linecap="round"><circle cx="8" cy="10" r="6.5"/><path d="M5 9.5l3 3 8-10"/></svg>Switchboard Maintenance/Upgrades</li>
      <li><svg width="18" height="18" viewBox="0 0 18 18" fill="none" stroke="var(--blue)" stroke-width="2.4" stroke-linecap="round"><circle cx="8" cy="10" r="6.5"/><path d="M5 9.5l3 3 8-10"/></svg>General electrical</li>
      <li><svg width="18" height="18" viewBox="0 0 18 18" fill="none" stroke="var(--blue)" stroke-width="2.4" stroke-linecap="round"><circle cx="8" cy="10" r="6.5"/><path d="M5 9.5l3 3 8-10"/></svg>Fire detection/warning systems</li>
    </ul>
  </aside>

  <footer class="contact">
    <svg class="contact-tab" viewBox="0 0 182 142"><polygon points="0,0 164,0 164,56 182,71 164,86 164,142 0,142" fill="var(--orange)"/></svg>
    <div class="contact-dot"></div>
    <h2 class="contact-title">CONTACT US FOR <span>MORE INFORMATION</span></h2>
    <div class="contact-item" style="left:198px; top:60px">
      <svg width="22" height="30" viewBox="0 0 22 30" fill="none" stroke="#fff" stroke-width="2"><path d="M11 3c-4 0-7 3-7 7 0 5 7 12 7 12s7-7 7-12c0-4-3-7-7-7z"/><circle cx="11" cy="10" r="2.5"/><ellipse cx="11" cy="25" rx="8" ry="3"/></svg>
      <div><p style="margin:0">41 Harlow Street,<br>Oakleigh, VIC, 3166</p></div>
    </div>
    <div class="contact-item" style="left:413px; top:57px">
      <svg width="16" height="50" viewBox="0 0 16 50" fill="#fff"><path d="M4 2l4-1 2 6-3 2c0 4 1 7 3 9l3-1 2 5-4 2C5 22 2 12 4 2z"/><path d="M4 29l4-1 2 6-3 2c0 4 1 7 3 9l3-1 2 5-4 2C5 49 2 39 4 29z"/></svg>
      <div><p>+61 (03) 5550 1240</p><p>+61 (03) 5550 1248</p></div>
    </div>
    <div class="contact-item" style="left:622px; top:55px">
      <svg width="22" height="50" viewBox="0 0 22 50" fill="none" stroke="#fff" stroke-width="2"><rect x="1" y="4" width="20" height="13" fill="#fff"/><path d="M1 4l10 8 10-8" stroke="var(--blue)"/><circle cx="11" cy="37" r="9"/><ellipse cx="11" cy="37" rx="4" ry="9"/><line x1="2" y1="37" x2="20" y2="37"/></svg>
      <div><p>electricalservices@corvelma.com.au</p><p>www.corvelmapower.com.au</p></div>
    </div>
  </footer>
</div>
</body>
</html>
```